Roof Plumbing Company needs simple, modern business card using the attached logo and below details:

Dean Halloway
Summit Gutters Pty Ltd
ABN: 58 214 937 062
Phone: 0417 286 531
Email: summitgutters@mailbrook.com
Website: summitgutters.com.au

For all of your metal roof plumbing requirements contact Summit Gutters for an obligation free quote - no job too big or to small!

Industry/Entity Type

Business

Contact Information for Business Card

Dean Halloway
Summit Gutters Pty Ltd
ABN 58 214 937 062
0417 286 531
summitgutters@mailbrook.com
summitgutters.com.au

Requirements
Must have
• Bright eye catching design, professional look

```html
<!DOCTYPE html>
<html lang="en">
<head>
<meta charset="utf-8">
<title>Summit Gutters – Business Card</title>
<link rel="stylesheet" href="https://fonts.googleapis.com/css2?family=Montserrat:wght@400;500;700&display=swap">
<style>
  :root {
    --bg: #e9e7e4;
    --card: #f7f7f7;
    --red: #d8141c;
    --red-dark: #b70f16;
    --charcoal: #2a2a2c;
    --ink: #3a3a3c;
    --white: #ffffff;
  }
  * { box-sizing: border-box; margin: 0; padding: 0; }
  html, body { width: 1200px; height: 800px; overflow: hidden; }
  body {
    background: var(--bg);
    font-family: "Montserrat", Arial, sans-serif;
    display: flex;
    align-items: center;
    justify-content: center;
    gap: 48px;
  }
  .card {
    position: relative;
    width: 540px;
    height: 310px;
    background: var(--card);
    overflow: hidden;
    box-shadow: 0 10px 28px rgba(0,0,0,0.18);
  }

  /* Front */
  .card-front .brand {
    position: absolute;
    top: 0; left: 0; right: 0;
    height: 205px;
    display: flex;
    align-items: center;
    justify-content: center;
    flex-direction: column;
    text-align: center;
  }
  .brand-name {
    color: var(--red);
    font-weight: 700;
    font-size: 30px;
    letter-spacing: 1px;
    text-transform: uppercase;
    line-height: 1.15;
  }
  .card-front .red-band {
    position: absolute;
    left: 0; right: 0; bottom: 0;
    height: 105px;
    background: linear-gradient(90deg, var(--red-dark), var(--red));
  }

  /* Back */
  .card-back .brand {
    position: absolute;
    top: 22px; left: 0; right: 0;
    text-align: center;
  }
  .card-back .brand-name { font-size: 20px; }
  .person-name {
    position: absolute;
    top: 84px; left: 0; right: 0;
    text-align: center;
    color: var(--ink);
    font-size: 18px;
    font-weight: 500;
  }
  .abn-band {
    position: absolute;
    top: 114px; left: 150px; right: 150px;
    height: 26px;
    background: var(--red);
    color: var(--white);
    font-size: 13px;
    letter-spacing: 0.5px;
    display: flex;
    align-items: center;
    justify-content: center;
  }
  .accent-stripe {
    position: absolute;
    top: 160px; left: 0; right: 0;
    height: 12px;
    background: var(--red);
  }
  .contact-panel {
    position: absolute;
    left: 0; right: 0; bottom: 0;
    height: 100px;
    background: var(--charcoal);
    display: flex;
    justify-content: space-between;
    align-items: flex-start;
    padding: 0 28px;
  }
  .contact-item {
    display: flex;
    flex-direction: column;
    align-items: center;
    margin-top: -17px;
  }
  .contact-icon {
    width: 34px; height: 34px;
    border-radius: 50%;
    background: var(--charcoal);
    border: 2px solid var(--red);
    display: flex;
    align-items: center;
    justify-content: center;
  }
  .contact-icon svg { width: 16px; height: 16px; }
  .contact-text {
    margin-top: 18px;
    color: var(--white);
    font-size: 12px;
    white-space: nowrap;
  }
</style>
</head>
<body>

  <section class="card card-front" aria-label="Business card front">
    <div class="brand">
      <div class="brand-name">Summit Gutters<br>Pty Ltd</div>
    </div>
    <div class="red-band"></div>
  </section>

  <section class="card card-back" aria-label="Business card back">
    <div class="brand">
      <div class="brand-name">Summit Gutters Pty Ltd</div>
    </div>
    <div class="person-name">Dean Halloway</div>
    <div class="abn-band">ABN 58 214 937 062</div>
    <div class="accent-stripe"></div>

    <div class="contact-panel">
      <div class="contact-item">
        <span class="contact-icon">
          <svg viewBox="0 0 24 24" fill="#fff" aria-hidden="true"><path d="M6.6 10.8a15.1 15.1 0 0 0 6.6 6.6l2.2-2.2a1 1 0 0 1 1-.25 11.4 11.4 0 0 0 3.6.57 1 1 0 0 1 1 1V20a1 1 0 0 1-1 1A17 17 0 0 1 3 4a1 1 0 0 1 1-1h3.5a1 1 0 0 1 1 1c0 1.25.2 2.45.57 3.6a1 1 0 0 1-.25 1z"/></svg>
        </span>
        <span class="contact-text">0417 286 531</span>
      </div>
      <div class="contact-item">
        <span class="contact-icon">
          <svg viewBox="0 0 24 24" fill="none" stroke="#fff" stroke-width="2" aria-hidden="true"><circle cx="12" cy="12" r="9"/><path d="M3 12h18M12 3c3 3.2 3 14.8 0 18M12 3c-3 3.2-3 14.8 0 18"/></svg>
        </span>
        <span class="contact-text">summitgutters.com.au</span>
      </div>
      <div class="contact-item">
        <span class="contact-icon">
          <svg viewBox="0 0 24 24" fill="none" stroke="#fff" stroke-width="2" aria-hidden="true"><rect x="3" y="5" width="18" height="14" rx="1"/><path d="M3 6l9 7 9-7"/></svg>
        </span>
        <span class="contact-text">summitgutters@mailbrook.com</span>
      </div>
    </div>
  </section>

</body>
</html>
```